Australian Skilled Migration

We need to design a add/flyer for a newspaper/magazine to promote our Australian Migration firm services. We targeting overseas graduating students and professionals who would like to Permanently Migrate to Australia.

We would like to advertise following services to our potential clients:

AUSTRALIA NEEDS YOU!!!

# Are you young and energetic individual?
# Do you have qualifications, work experiences or both?
# Perhaps you would like to open a small business, and sponsor yourself to live in Australia?
# Aspiring for job security and the highest living standards?

Contact us to find out how we can help you with Permanent Migration to Australia.

First consultation and eligibility assessment is free ! Tell your friends about us and receive a discount on your future fees!!

For more information please visit our website: www.pelmora-links.org.au

(for a background we would like to use Australian themes such as: sandy beaches, ect... light colours)

Target Market(s)

Students
University graduates
Trade people with qualifications
Industry professionals
Anyone who wants to migrate to Australia

Industry/Entity Type

Security

Requirements
Must have
• our logo and website
easy to see and read the txt

Catchy Background
Nice to have
• as per our requirements
(designer questions, please e-mail: info@pelmora-links.org. au)

```html
<!DOCTYPE html>
<html lang="en">
<head>
<meta charset="utf-8">
<title>Australia Need You – Permanent Migration Flyer</title>
<link href="https://fonts.googleapis.com/css2?family=Archivo+Black&family=Kalam:wght@700&family=Arimo:wght@700&display=swap" rel="stylesheet">
<style>
  :root {
    --navy: #24336b;
    --red: #e0262b;
    --white: #ffffff;
    --sand: #efe9dc;
    --sea: #4fb7c4;
    --glow: #eeeac0;
    --logo-red: #c8242a;
  }
  * { margin: 0; padding: 0; box-sizing: border-box; }
  html, body { width: 933px; height: 1200px; overflow: hidden; background: var(--white); }
  .flyer { position: relative; width: 933px; height: 1200px; overflow: hidden; font-family: "Arimo", Arial, sans-serif; }

  .hero { position: absolute; left: 0; top: 0; width: 933px; height: 608px; }
  .hero-scene {
    position: absolute; inset: 0;
    background: linear-gradient(170deg, #3aa9b8 0%, #7fcfd3 6%, #f3f0e8 16%, #ece6d8 55%, #d9d0bd 100%);
  }
  .hero-glow {
    position: absolute; left: -380px; top: -150px; width: 1000px; height: 830px; border-radius: 50%;
    background: radial-gradient(circle at 45% 50%, rgba(255,255,255,0.85) 0%, rgba(246,244,224,0.9) 40%, var(--glow) 72%, rgba(238,234,192,0.6) 100%);
  }

  .headline { position: absolute; left: 40px; top: 34px; font-family: "Archivo Black", "Arial Black", sans-serif; line-height: 1; }
  .headline span {
    display: block; letter-spacing: 1px;
    -webkit-text-stroke: 8px var(--white); paint-order: stroke fill;
  }
  .headline .line-country { color: var(--navy); font-size: 84px; }
  .headline .line-call { color: var(--red); font-size: 90px; margin-top: 8px; }

  .questions { position: absolute; left: 42px; top: 242px; width: 520px; color: var(--navy);
    font-family: "Kalam", "Comic Sans MS", cursive; font-weight: 700; font-size: 22px; line-height: 29px; transform: skewX(-6deg); }
  .questions p { margin-bottom: 28px; }

  .firm-mark { position: absolute; left: 623px; top: 522px; width: 310px; height: 68px; background: var(--white);
    display: flex; align-items: center; gap: 10px; padding-left: 16px; }
  .firm-mark .dot { width: 40px; height: 40px; border-radius: 50%; border: 2px solid var(--logo-red); flex: none; }
  .firm-mark .name { color: var(--logo-red); font-family: "Arimo", Arial, sans-serif; font-size: 15px; line-height: 1.2; }

  .offer { position: absolute; left: 0; top: 608px; width: 933px; height: 383px; background: var(--navy);
    color: var(--white); text-align: center; font-weight: 700; }
  .offer .contact { margin-top: 16px; font-size: 24px; line-height: 27px; }
  .offer .country { margin-top: 14px; font-size: 44px; letter-spacing: 2px; line-height: 48px; }
  .offer .free { margin-top: 8px; font-size: 22px; }
  .offer .referral { margin-top: 20px; font-size: 24px; line-height: 25px; }
  .offer .more { margin-top: 22px; font-size: 24px; line-height: 25px; }
  .offer .website { margin-top: 10px; font-size: 50px; letter-spacing: 2px; }

  .flag-band { position: absolute; left: 0; top: 991px; width: 933px; height: 209px;
    background: linear-gradient(100deg, #b9222e 0%, #e9e4ea 18%, #2f3f8e 35%, #1f2c73 60%, #2c3c86 80%, #1e2a6b 100%); }
</style>
</head>
<body>
<main class="flyer">
  <section class="hero">
    <div class="hero-scene" role="img" aria-label="Sunny white sand beach with turquoise sea and a wooden sun lounger"></div>
    <div class="hero-glow"></div>
    <h1 class="headline"><span class="line-country">AUSTRALIA</span><span class="line-call">NEED YOU!!!</span></h1>
    <div class="questions">
      <p>Are you young and energetic individual?</p>
      <p>Do you have qualifications, work<br>experiences or both?</p>
      <p>Perhaps you would like to open a small<br>business,and sponsor yourself to live in<br>Australia?</p>
      <p>Aspiring for job security and the highest<br>living standards?</p>
    </div>
    <div class="firm-mark"><span class="dot"></span><span class="name">Harlow &amp; Reed<br>Lawyers &amp; Migration Agents</span></div>
  </section>

  <section class="offer">
    <p class="contact">Contact us to find out how we can help you &nbsp;with<br>PERMANENT MIGRATION TO</p>
    <p class="country">AUSTRALIA</p>
    <p class="free">First consultation and eligibility assessment is free !</p>
    <p class="referral">Tell your friends about us and receive<br>a discount on your future fees!!</p>
    <p class="more">For more information<br>please visit our website:</p>
    <p class="website">www.pelmora-links.org.au</p>
  </section>

  <div class="flag-band" role="img" aria-label="Australian flag waving in the wind"></div>
</main>
</body>
</html>
```